I am a company selling interior designing materials

HI, I am selling interior design materials and require a namecard which is more outstanding while following a certain details placement as attached.

My clients are mainly interior designers so it has to attract their attention rather than feeling that its "just another namecard". I am selling wallcoverings, fabrics, acoustics and carpets.

Target Market(s)

interior designers designing hotels, commerical offices.

Contact Information for Business Card

As per attached.
Please change address to 47 Jalan 16 Tampines #05-02 Velmora Building Singapore 527314

Font styles to use
Other font styles liked:
• calibri

Requirements
Must have
• (1) company logo on top in the middle. Placement of contac details to be the same
• (2) company color is blue/green cymk 75/8/42/0
• (3) "KTV" logo to be prominent
• (4) You may change the logo but there should be a "swirl" surrounding the word KTV like current logo. The swirl pattern does not need to follow current logo and you may propose.
Should not have
• (1) there should not be any designs above "KTV" logo
• (2) no sharp triangles or angles

```html
<!DOCTYPE html>
<html lang="en">
<head>
<meta charset="utf-8">
<title>KTV Business Card</title>
<link rel="stylesheet" href="https://fonts.googleapis.com/css2?family=Carlito:wght@700&family=Nunito:wght@600;700&family=Roboto+Slab:wght@700&display=swap">
<style>
  :root {
    --backdrop: #2b2b2b;
    --paper-light: #fbfbfb;
    --paper-mid: #e9e9e9;
    --paper-dark: #b9b9b9;
    --teal: #1eb0a0;
    --teal-deep: #137a6e;
    --accent-red: #e0202a;
    --slate: #5e5e5e;
    --ink: #505050;
    --white: #ffffff;
  }
  html, body {
    margin: 0;
    padding: 0;
    width: 1200px;
    height: 960px;
    overflow: hidden;
    background: var(--backdrop);
  }
  .card {
    position: absolute;
    width: 600px;
    height: 341px;
    overflow: hidden;
    box-shadow: 0 4px 10px rgba(0,0,0,0.45);
  }
  .card--front { left: 303px; top: 125px; }
  .card--back  { left: 299px; top: 493px; height: 342px; }
  .card__art {
    position: absolute;
    inset: 0;
    width: 100%;
    height: 100%;
  }
  .wordmark {
    position: absolute;
    left: 0;
    width: 100%;
    text-align: center;
    font-family: "Roboto Slab", Georgia, serif;
    font-weight: 700;
    color: var(--slate);
    line-height: 1;
    letter-spacing: -1px;
  }
  .card--front .wordmark { top: 60px; font-size: 46px; }
  .card--back .wordmark  { top: 108px; font-size: 60px; }
  .company-name {
    position: absolute;
    top: 129px;
    left: 0;
    width: 100%;
    text-align: center;
    font-family: "Carlito", Calibri, Arial, sans-serif;
    font-weight: 700;
    font-size: 16px;
    color: var(--ink);
  }
  .person-name {
    position: absolute;
    top: 178px;
    left: 0;
    width: 100%;
    text-align: center;
    font-family: "Roboto Slab", Georgia, serif;
    font-weight: 700;
    font-size: 19px;
    color: var(--teal);
    letter-spacing: 0.5px;
  }
  .person-mobile {
    position: absolute;
    top: 201px;
    left: 0;
    width: 100%;
    text-align: center;
    font-family: "Nunito", Arial, sans-serif;
    font-weight: 700;
    font-size: 14px;
    color: var(--ink);
  }
  .contact {
    position: absolute;
    top: 284px;
    font-family: "Nunito", Arial, sans-serif;
    font-weight: 700;
    font-size: 14.5px;
    line-height: 20px;
    color: var(--white);
  }
  .contact--address { left: 28px; }
  .contact--office { right: 34px; text-align: right; }
  .product-line {
    position: absolute;
    top: 297px;
    left: 0;
    width: 100%;
    text-align: center;
    font-family: "Nunito", Arial, sans-serif;
    font-weight: 700;
    font-size: 15.5px;
    color: var(--white);
  }
</style>
</head>
<body>

<section class="card card--front">
  <svg class="card__art" viewBox="0 0 600 341" preserveAspectRatio="none" aria-hidden="true">
    <defs>
      <linearGradient id="paperFront" x1="0" y1="0" x2="1" y2="0.3">
        <stop offset="0" stop-color="var(--paper-mid)"/>
        <stop offset="0.45" stop-color="var(--paper-light)"/>
        <stop offset="1" stop-color="var(--paper-dark)"/>
      </linearGradient>
      <linearGradient id="tealFront" x1="0" y1="0" x2="1" y2="0">
        <stop offset="0" stop-color="var(--teal)"/>
        <stop offset="0.6" stop-color="var(--teal)"/>
        <stop offset="1" stop-color="var(--teal-deep)"/>
      </linearGradient>
    </defs>
    <rect width="600" height="341" fill="url(#paperFront)"/>
    <path d="M0,247 C200,262 380,252 480,206 L480,341 L0,341 Z" fill="var(--slate)"/>
    <path d="M0,258 C260,266 480,236 600,121 L600,341 L0,341 Z" fill="var(--accent-red)"/>
    <path d="M0,268 C270,272 490,248 600,131 L600,341 L0,341 Z" fill="url(#tealFront)"/>
  </svg>
  <div class="wordmark">KTV</div>
  <div class="company-name">KenTavio Interior Furnishings Pte Ltd</div>
  <div class="person-name">LENA CHUA</div>
  <div class="person-mobile">(65) 9127 4410</div>
  <div class="contact contact--address">47 Jalan 16 Tampines #05-02<br>Velmora Building Singapore 527314</div>
  <div class="contact contact--office">(65) 6782 3051<br>lena@ktvfurnishing.com</div>
</section>

<section class="card card--back">
  <svg class="card__art" viewBox="0 0 600 342" preserveAspectRatio="none" aria-hidden="true">
    <defs>
      <linearGradient id="paperBack" x1="0" y1="0" x2="1" y2="0.3">
        <stop offset="0" stop-color="var(--paper-mid)"/>
        <stop offset="0.45" stop-color="var(--paper-light)"/>
        <stop offset="1" stop-color="var(--paper-dark)"/>
      </linearGradient>
      <linearGradient id="tealBack" x1="0" y1="0" x2="1" y2="0">
        <stop offset="0" stop-color="var(--teal)"/>
        <stop offset="0.6" stop-color="var(--teal)"/>
        <stop offset="1" stop-color="var(--teal-deep)"/>
      </linearGradient>
    </defs>
    <rect width="600" height="342" fill="url(#paperBack)"/>
    <path d="M0,250 C200,264 380,254 480,208 L480,342 L0,342 Z" fill="var(--slate)"/>
    <path d="M0,261 C260,268 480,238 600,124 L600,342 L0,342 Z" fill="var(--accent-red)"/>
    <path d="M0,270 C270,274 490,250 600,134 L600,342 L0,342 Z" fill="url(#tealBack)"/>
  </svg>
  <div class="wordmark">KTV</div>
  <div class="product-line">Wallcoverings • Acoustic • Fabrics • Carpet</div>
</section>

</body>
</html>
```